Law firm needs business card and letter head designed

I need a business card and a letter head for a law firm, well its not really a law firm as it is just me.
The letter head is to have the logo located on the top right hand side, with a footer designed as well. The footer will also be on the second page but the main logo design will not be on the second page.

The business card is to be doubled sided.

The business name is Corvane Legal.

Industry/Entity Type

Legal

Requirements
Must have
• The letterhead is to have the logo top right hand side of the front page with email address tbrook@corvanelegal.com.au and phone number 0417 362 851, with a footer designed that incorporates the logo, the footer is also to include the following wording Liability Limited by a scheme approved under Professional Standards Legislation.
• I would like the letterhead design to have a second page, with this page just having the footer design, the second page does not need to have the wording above.
• The business card is to be double sides, with one side having my name Tobias Brook and title Principal, along with the number 0417 362 851 and the email tbrook@corvanelegal.com.au
• I would like a classy design but with some edge.

```html
<!DOCTYPE html>
<html lang="en">
<head>
<meta charset="utf-8">
<title>Corvane Legal — Letterhead</title>
<link rel="stylesheet" href="https://fonts.googleapis.com/css2?family=Source+Sans+3:wght@400;600&family=Lato:ital,wght@1,400&display=swap">
<style>
  :root {
    --backdrop: #5a5b5a;
    --paper-light: #f7f7f7;
    --paper: #e6e6e6;
    --teal: #176e8c;
    --ink: #3e3e3e;
    --rule-grey: #9a9a9a;
    --white: #ffffff;
  }
  * { margin: 0; padding: 0; box-sizing: border-box; }
  html, body { width: 1200px; height: 793px; overflow: hidden; background: var(--backdrop); }
  .canvas { position: relative; width: 1200px; height: 793px; font-family: "Source Sans 3", Arial, sans-serif; color: var(--ink); }
  .sheet {
    position: absolute; top: 34px; width: 515px; height: 724px; overflow: hidden;
    background: radial-gradient(ellipse 70% 60% at 10% 55%, var(--paper-light), var(--paper) 70%);
    box-shadow: 0 1px 3px rgba(0,0,0,.35);
  }
  .sheet--first { left: 68px; }
  .sheet--second { left: 615px; }

  .contact { position: absolute; left: 51px; top: 71px; list-style: none; font-size: 9.6px; line-height: 14px; }
  .contact li { display: flex; align-items: center; gap: 4px; }
  .contact svg { width: 9px; height: 9px; flex: none; }

  .brand { position: absolute; display: flex; align-items: center; gap: 5px; color: var(--teal); font-weight: 600; letter-spacing: .3px; }
  .brand__mark { width: 9px; height: 9px; background: var(--teal); }
  .brand--head { right: 49px; top: 127px; font-size: 11.5px; }
  .brand--foot { right: 22px; top: 668px; font-size: 9px; }

  .letter { position: absolute; left: 55px; top: 259px; width: 409px; }
  .letter__salutation { font-size: 13px; margin-bottom: 21px; }
  .letter__body p { font-size: 8.5px; line-height: 11.6px; text-align: justify; margin-bottom: 11.6px; }
  .letter__closing { font-size: 8.5px; margin-top: 12px; }
  .signature { display: block; width: 64px; height: 26px; margin: 10px 0 0 0; background: linear-gradient(90deg, rgba(30,30,40,.12), rgba(30,30,40,.25)); border-radius: 2px; }
  .signatory { margin: 4px 0 0 16px; font-family: Arial, sans-serif; }
  .signatory__name { font-size: 9px; color: var(--teal); letter-spacing: .2px; }
  .signatory__title { font-size: 6.5px; color: var(--ink); }

  .footer { position: absolute; left: 0; bottom: 0; width: 515px; height: 50px; }
  .footer svg { position: absolute; inset: 0; }
  .footer__note { position: absolute; left: 0; right: 30px; bottom: 8px; text-align: center; font-family: "Lato", Arial, sans-serif; font-style: italic; font-size: 9px; color: var(--white); }
</style>
</head>
<body>
<div class="canvas">

  <section class="sheet sheet--first" aria-label="Letterhead, page one">
    <ul class="contact">
      <li><svg viewBox="0 0 10 10"><circle cx="5" cy="5" r="5" fill="var(--teal)"/><path d="M3 2.6l1 .1.5 1.3-.6.5c.4.8 1 1.4 1.8 1.8l.5-.6 1.3.5.1 1c-.5.5-3 .7-4.9-1.2C2 4.6 2.4 3 3 2.6z" fill="#fff"/></svg>0417 362 851</li>
      <li><svg viewBox="0 0 10 10"><circle cx="5" cy="5" r="5" fill="var(--teal)"/><rect x="2.3" y="3" width="5.4" height="4" rx=".5" fill="#fff"/><path d="M2.5 3.3L5 5.2l2.5-1.9" stroke="var(--teal)" stroke-width=".7" fill="none"/></svg>tbrook@corvanelegal.com.au</li>
      <li><svg viewBox="0 0 10 10"><circle cx="5" cy="5" r="5" fill="var(--teal)"/><circle cx="5" cy="5" r="2.7" fill="none" stroke="#fff" stroke-width=".8"/><path d="M2.3 5h5.4M5 2.3v5.4" stroke="#fff" stroke-width=".6"/></svg>www.corvanelegal.com.au</li>
    </ul>

    <div class="brand brand--head"><span class="brand__mark"></span>CORVANE LEGAL</div>

    <article class="letter">
      <p class="letter__salutation">Dear Mr. Harlow,</p>
      <div class="letter__body">
        <p>Lorem ipsum dolor sit amet, consectetur adipiscing elit. Donec orci purus, luctus vitae dignissim eu, iaculis sed purus. Vivamus faucibus, ipsum nec aliquet viverra, leo mauris condimentum ligula, sit amet sagittis enim ligula quis arcu. Nam egestas tortor id nisi porttitor mattis. In tortor ante, ultricies in suscipit a, tempus non massa. Vivamus et auctor mi. Fusce vel massa nulla. Phasellus nec eros mauris, et scelerisque orci.</p>
        <p>Donec malesuada orci vitae nulla accumsan porta a id massa. Quisque accumsan iaculis magna sit amet fringilla. Maecenas consequat, magna eget tincidunt semper, odio nibh rutrum mi, id feugiat ante nisi eu risus. Vestibulum nunc orci, rhoncus a placerat in, ultricies in mi. Cras mattis varius eros, vel fringilla nisi suscipit eget. Quisque scelerisque sagittis nulla at porttitor.</p>
        <p>Sed id augue vitae urna euismod commodo aliquet a quam. Pellentesque arcu velit, cursus et malesuada ut, consequat et diam. Nullam erat sem, rhoncus id ullamcorper vitae, rhoncus et arcu. In ultricies ultricies nulla, ut rutrum nisi iaculis at. Donec eu magna a metus ornare faucibus. Fusce aliquet faucibus ultricies. Morbi semper, est id tincidunt gravida, sem arcu adipiscing lacus, ac bibendum nulla leo eu purus. Quisque nec diam sed risus consectetur a ccumsan quis quis nibh. Vestibulum id purus lorem.</p>
        <p>It is a long established fact that a reader will be distracted by the readable content of a page when looking at its layout. The point of using Lorem Ipsum is that it has a more-or-less normal distribution of letters, as opposed to using 'Content here, content here', making it look like readable English. Many desktop publishing packages</p>
      </div>
      <p class="letter__closing">Sincerely,</p>
      <span class="signature" role="img" aria-label="Handwritten signature"></span>
      <div class="signatory">
        <p class="signatory__name">TOBIAS BROOK</p>
        <p class="signatory__title">CEO/Founder</p>
      </div>
    </article>

    <footer class="footer">
      <svg viewBox="0 0 515 50" preserveAspectRatio="none" aria-hidden="true">
        <path d="M0 29 Q240 -2 515 43" fill="none" stroke="var(--rule-grey)" stroke-width="2.5"/>
        <path d="M0 36 Q240 6 515 48 L515 50 L0 50 Z" fill="var(--teal)"/>
      </svg>
      <p class="footer__note">Liability Limited by a scheme approved under Professional Standards Legislation.</p>
    </footer>
  </section>

  <section class="sheet sheet--second" aria-label="Letterhead, page two">
    <div class="brand brand--foot"><span class="brand__mark"></span>CORVANE LEGAL</div>
    <footer class="footer">
      <svg viewBox="0 0 515 50" preserveAspectRatio="none" aria-hidden="true">
        <path d="M0 29 Q240 -2 515 43" fill="none" stroke="var(--rule-grey)" stroke-width="2.5"/>
        <path d="M0 36 Q240 6 515 48 L515 50 L0 50 Z" fill="var(--teal)"/>
      </svg>
    </footer>
  </section>

</div>
</body>
</html>
```